Plakat-Design für Blasmusik Konzert
Zielgruppe
Wir - die Tordinger Blasmusik e.V. - sind auf der Suche nach:
einem Plakatdesign in A1 & A2 und passendem
Ticket-Design DIN lang quer inkl. Perforierung und 2x Nummerierung
für unser Konzert 2019 mit dem Motto:
'NIGHTS OF WONDER'.
Das Konzert wird einen weiten Rahmen von Henrik Dallmann und Brisko hin zu Bernd Falkenrath und Tom Kellin. Auch Titel aus dem Bereich Filmmusik wird es geben. Also ein bunter Abend mit Gesang und Showlicht.
Wir freuen uns auf eure Ideen!!!
Impressionen: www.tordinger-blasmusik.de
Aufgabenstellung
Stichworte: Bunt, Modern, Edel
Facts:
Samstag 05.10.2019 Beginn 19:00
Aula im Schulzentrum, Tordingen am See
Eintritt 15€, Kinder bis einschließlich 8 Jahre Eintritt frei.
'Mehr Informationen unter www.tordinger-blasmusik.de und auf Plaudernet'
Für Ticket: Einlass ab 18:30 Uhr. Freie Platzwahl.
Irgendwo auf dem Plakat muss Platz für die dezente Nennung von 2-3 Sponsoren vorgesehen werden. Diese würden wir nachträglich einfügen. Auch ein 'Find us on Plaudernet'-Icon wäre cool.
Die Druckdateien (CMYK) sind mit entsprechendem Beschnitt gemäß Vorgabe von 'flott-gedruckt-jetzt' anzulegen und als Vector-Datei sowie PDF zu übergeben.

```html
<!DOCTYPE html>
<html lang="de">
<head>
<meta charset="utf-8">
<title>Nights of Wonder – Konzert 2019</title>
<link rel="stylesheet" href="https://fonts.googleapis.com/css2?family=Fira+Sans:ital,wght@0,500;0,600;1,500;1,600&family=Great+Vibes&display=swap">
<style>
  :root {
    --page: #3a3d40;
    --poster-red: #8c1f27;
    --cream: #f1d7a4;
    --gold-light: #f6e3bc;
    --band-a: #f8e8c4;
    --band-b: #ecd29f;
    --ink-dark: #6a1418;
    --white: #ffffff;
  }
  * { margin: 0; padding: 0; box-sizing: border-box; }
  html, body { width: 1200px; height: 1200px; overflow: hidden; background: var(--page); }
  .poster {
    position: absolute; left: 200px; top: 30px; width: 800px; height: 1140px;
    background: var(--poster-red); color: var(--cream);
    font-family: "Fira Sans", sans-serif; overflow: hidden;
  }
  .club-name {
    position: absolute; left: 26px; top: 60px; font-weight: 600; font-style: italic;
    color: var(--cream); line-height: 1;
  }
  .club-name .line-1 { display: block; font-size: 38px; }
  .club-name .line-2 { display: block; font-size: 28px; margin-top: 4px; }
  .club-name .year { font-size: 16px; margin-right: 8px; }
  .date-box {
    position: absolute; right: 14px; top: 36px; height: 56px; padding: 0 14px;
    background: var(--gold-light); color: var(--ink-dark);
    font-size: 40px; font-weight: 500; line-height: 56px;
  }
  .venue {
    position: absolute; right: 22px; top: 96px; text-align: right;
    font-size: 26px; font-style: italic; font-weight: 500; line-height: 33px;
  }
  .start-time {
    position: absolute; right: 22px; top: 166px; font-size: 38px; font-weight: 600; font-style: italic;
  }
  .concert-visual { position: absolute; left: 20px; top: 186px; width: 740px; height: 630px; }
  .motto {
    position: absolute; left: 0; width: 800px; text-align: center;
    font-family: "Great Vibes", cursive; color: var(--cream); line-height: 1;
  }
  .motto-top { top: 440px; font-size: 150px; }
  .motto-bottom { top: 615px; font-size: 150px; padding-left: 30px; }
  .concert-year {
    position: absolute; top: 812px; width: 800px; text-align: center;
    font-size: 56px; font-weight: 600;
  }
  .programme {
    position: absolute; top: 906px; width: 800px; text-align: center;
    font-size: 21px; font-weight: 500; line-height: 28px;
  }
  .programme .mood { font-style: italic; }
  .admission {
    position: absolute; top: 1002px; left: 26px; right: 20px;
    font-size: 14.5px; font-style: italic; font-weight: 500; white-space: nowrap;
  }
  .info-band {
    position: absolute; left: 0; bottom: 0; width: 800px; height: 102px;
    background: linear-gradient(90deg, var(--band-a), var(--band-b) 55%, var(--band-a));
    color: var(--ink-dark);
  }
  .info-band .label { position: absolute; left: 12px; top: 10px; font-size: 13px; font-style: italic; font-weight: 500; }
  .info-band .social { position: absolute; left: 12px; top: 38px; font-size: 19px; font-style: italic; font-weight: 500; }
  .info-band .social .dot {
    display: inline-block; width: 13px; height: 13px; background: var(--ink-dark);
    margin-right: 6px; vertical-align: -1px;
  }
  .info-band .website { position: absolute; left: 12px; top: 64px; font-size: 19px; font-style: italic; font-weight: 500; }
  .sponsor {
    position: absolute; top: 10px; width: 126px; height: 78px; background: var(--white);
    color: #111; font-size: 20px; font-weight: 600; display: flex; align-items: center; justify-content: center;
  }
  .sponsor-one { left: 514px; }
  .sponsor-two { left: 652px; }
</style>
</head>
<body>
  <main class="poster">
    <div class="club-name">
      <span class="line-1">Tordinger</span>
      <span class="line-2"><span class="year">1986</span>Blasmusik e.V.</span>
    </div>
    <div class="date-box">Sa. 05.10.2019</div>
    <div class="venue">Aula im Schulzentrum,<br>Tordingen am See</div>
    <div class="start-time">Beginn: 19.00</div>

    <svg class="concert-visual" viewBox="0 0 740 630" role="img" aria-label="Foto des Orchesters auf der Bühne mit Showlicht, in Umrisse von Blasinstrumenten gesetzt">
      <defs>
        <radialGradient id="stageGlow" cx="50%" cy="40%" r="65%">
          <stop offset="0" stop-color="#b46a55"/>
          <stop offset="0.5" stop-color="#5e2226"/>
          <stop offset="1" stop-color="#3a1416"/>
        </radialGradient>
      </defs>
      <path d="M40 150 C 120 80 220 40 330 40 C 420 40 460 120 520 110 C 600 90 660 60 720 150 C 730 260 710 360 640 440 C 560 520 470 600 370 610 C 270 600 170 540 110 450 C 60 360 30 260 40 150 Z" fill="url(#stageGlow)"/>
    </svg>

    <div class="motto motto-top">Nights</div>
    <div class="motto motto-bottom">of Wonder</div>

    <div class="concert-year">Konzert 2019</div>
    <div class="programme">
      Henrik Dallmann…Brisko…Bernd Falkenrath…Tom Kellin<br>
      <span class="mood">Bunter Abend mit Gesang und Showlicht</span>
    </div>
    <div class="admission">Eintritt 15€, Kinder bis einschließlich 8 Jahre Eintritt frei. Für Ticket: Einlass ab 18:30 Uhr. Freie Platzwahl.</div>

    <footer class="info-band">
      <div class="label">Mehr Informationen :</div>
      <div class="social"><span class="dot"></span>plaudernet.com/Tordinger-Blasmusik-eV</div>
      <div class="website">www.tordinger-blasmusik</div>
      <div class="sponsor sponsor-one">Sonvero</div>
      <div class="sponsor sponsor-two">Kraftal</div>
    </footer>
  </main>
</body>
</html>
```